Engineering/Manufacturing Company Needs PowerPoint Update and Template

We want to update the look and feel of our current corporate overview PowerPoint. We would like a working template moving forward with 6-8 slide layouts as well as a couple cover page options. Our content ranges from basic bullet points to complex graphs, images, and a combination of those, so we need templates that will work with a wide variety of content.
Our company specializes in complex precision machining, Engineering, and Advanced heavy duty truck products. We would like this presentation to represent our high-level manufacturing technology.
Our corporate color is blue (RBG 26/75/159), and we also use gray and white. We are looking for a modern, clean, yet masculine/industrial feeling. I have included our company logo, but other than that we would like to see what you can come up with. We would like it to feel clean yet industrial.
Target Market(s)
High-level management in the manufacturing and heavy duty truck/bus industries.
Industry/Entity Type
Manufacturer

```html
<!DOCTYPE html>
<html lang="en">
<head>
<meta charset="utf-8">
<title>KVR Corporate Overview – Slide Template System</title>
<link rel="stylesheet" href="https://fonts.googleapis.com/css2?family=Open+Sans:wght@400;600;700;800&display=swap">
<style>
  :root{
    --canvas:#a7a8a9;
    --blue:#1a4b9f;
    --blue-dark:#123a7e;
    --blue-light:#3f6fbf;
    --grey:#6d6e71;
    --grey-mid:#9a9b9d;
    --grey-light:#e3e4e6;
    --paper:#ffffff;
    --ink:#3a3a3c;
  }
  *{box-sizing:border-box;margin:0;padding:0}
  html,body{width:1200px;height:1046px;overflow:hidden;background:var(--canvas)}
  body{position:relative;font-family:"Open Sans",Arial,sans-serif}
  .slide{position:absolute;width:237px;height:134px;background:var(--paper);box-shadow:0 1px 2px rgba(0,0,0,.25);overflow:hidden}
  .slide svg{display:block;width:100%;height:100%}
  .c1{left:98px}.c2{left:359px}.c3{left:617px}.c4{left:878px}
  .r1{top:76px}.r2{top:230px}.r3{top:384px}.r4{top:540px}.r5{top:692px}.r6{top:847px}
  svg text{font-family:"Open Sans",Arial,sans-serif}
  .title{font-size:5px;font-weight:700;fill:var(--ink)}
  .rule{stroke:var(--blue);stroke-width:.8}
  .p{font-size:2.6px;fill:var(--grey)}
  .pw{font-size:2.6px;fill:#fff}
  .h{font-size:3.6px;font-weight:700;fill:var(--blue)}
  .hw{font-size:3.6px;font-weight:700;fill:#fff}
  .lbl{font-size:3.2px;font-weight:600;fill:var(--ink)}
  .lblw{font-size:3px;font-weight:600;fill:#fff}
  .blue{fill:var(--blue)}
  .bdark{fill:var(--blue-dark)}
  .grey{fill:var(--grey)}
  .glight{fill:var(--grey-light)}
  .white{fill:#fff}
  .ico{fill:#fff}
  .icob{fill:var(--blue)}
  .mid{text-anchor:middle}
  .end{text-anchor:end}
</style>
</head>
<body>

<!-- 1. Cover -->
<section class="slide c1 r1" aria-label="Cover slide">
<svg viewBox="0 0 276 156">
  <defs>
    <linearGradient id="coverPhoto" x1="0" y1="0" x2="1" y2="1">
      <stop offset="0" stop-color="#2a5cb0"/><stop offset=".55" stop-color="#1a4b9f"/><stop offset="1" stop-color="#0f3478"/>
    </linearGradient>
  </defs>
  <rect width="276" height="156" fill="url(#coverPhoto)" role="img" aria-label="Blue-toned photo of a precision machining workstation"/>
  <path d="M22 0h62v34a6 6 0 0 1-6 6H28a6 6 0 0 1-6-6z" class="white"/>
  <text x="53" y="27" class="mid" style="font-size:13px;font-weight:800;fill:var(--blue)">KVR</text>
  <text x="234" y="119" class="end" style="font-size:11.5px;font-weight:700;fill:#fff">Edit title here</text>
  <line x1="241" y1="106" x2="241" y2="124" stroke="#fff" stroke-width=".8"/>
</svg>
</section>

<!-- 2. Text + columns -->
<section class="slide c2 r1" aria-label="Text and two column slide">
<svg viewBox="0 0 276 156">
  <text x="10" y="13" class="title">EDIT TITLE HERE</text><line x1="10" y1="16" x2="22" y2="16" class="rule"/>
  <rect x="0" y="30" width="170" height="116" class="glight"/>
  <g class="p">
    <text x="16" y="42">Lorem ipsum dolor sit amet,</text><text x="16" y="46">consectetur adipiscing elit. Donec</text>
    <text x="16" y="50">lorem ante, laoreet sit ac,</text><text x="16" y="54">sollicitudin maximus felis. Curabitur</text>
    <text x="16" y="58">ac purus a sapien auctor facilisis.</text><text x="16" y="62">dictum, turpis ac ultricies rutrum,</text>
    <text x="16" y="66">lectus sapien cursus est, vitae</text><text x="16" y="70">odio justo eget sem. Vestibulum</text>
    <text x="16" y="74">anim, ultricies quis placerat sed,</text><text x="16" y="78">aliquam eu ipsum. Sed a felis et</text>
    <text x="16" y="82">ullamcorper convallis eu id enim</text><text x="16" y="86">purus. Nam rhoncus risus a felis</text>
    <text x="16" y="90">maximus aliquam. Integer quis</text><text x="16" y="94">tincidunt libero, non tincidunt</text>
    <text x="16" y="98">ligula. Lorem ipsum dolor sit amet,</text><text x="16" y="102">consectetur adipiscing elit. Donec</text>
    <text x="16" y="106">lorem ante, laoreet sit amet.</text><text x="16" y="110">sollicitudin maximus felis. Curabitur</text>
    <text x="16" y="114">ac purus a sapien auctor facilisis.</text><text x="16" y="118">Sed dictum turpis ultricies.</text>
  </g>
  <rect x="88" y="36" width="78" height="96" class="blue"/>
  <rect x="166" y="36" width="80" height="96" class="bdark"/>
  <text x="127" y="46" class="hw mid">Lorem ipsum</text>
  <text x="206" y="46" class="hw mid">Lorem ipsum</text>
  <g class="pw">
    <text x="92" y="54">Lorem ipsum dolor sit amet,</text><text x="92" y="58">consectetur adipiscing elit. Donec</text>
    <text x="92" y="62">lorem ante, laoreet sit ac,</text><text x="92" y="66">sollicitudin maximus felis.</text>
    <text x="92" y="70">dictum, turpis ac ultricies rutrum,</text><text x="92" y="74">lectus sapien cursus est, vitae</text>
    <text x="92" y="78">odio justo eget sem. Vestibulum</text><text x="92" y="82">anim, ultricies quis placerat,</text>
    <text x="92" y="86">aliquam eu ipsum. Sed a felis</text><text x="92" y="90">ullamcorper convallis eu id</text>
    <text x="92" y="94">purus. Nam rhoncus risus felis</text><text x="92" y="98">maximus aliquam. Integer quis</text>
    <text x="92" y="102">tincidunt libero, non tincidunt.</text>
    <text x="170" y="54">Lorem ipsum dolor sit amet,</text><text x="170" y="58">consectetur adipiscing elit. Donec</text>
    <text x="170" y="62">lorem ante, laoreet sit ac,</text><text x="170" y="66">sollicitudin maximus felis.</text>
    <text x="170" y="70">dictum, turpis ac ultricies rutrum,</text><text x="170" y="74">lectus sapien cursus est, vitae</text>
    <text x="170" y="78">odio justo eget sem. Vestibulum</text><text x="170" y="82">anim, ultricies quis placerat,</text>
    <text x="170" y="86">aliquam eu ipsum. Sed a felis</text><text x="170" y="90">ullamcorper convallis eu id</text>
    <text x="170" y="94">purus. Nam rhoncus risus felis</text><text x="170" y="98">maximus aliquam. Integer quis</text>
  </g>
  <rect x="246" y="26" width="30" height="124" fill="#d7d9dd" role="img" aria-label="Photo of business people standing"/>
</svg>
</section>

<!-- 3. Matrix table -->
<section class="slide c3 r1" aria-label="Matrix slide">
<svg viewBox="0 0 276 156">
  <text x="10" y="13" class="title">EDIT TITLE HERE</text><line x1="10" y1="16" x2="22" y2="16" class="rule"/>
  <g class="blue">
    <rect x="60" y="30" width="36" height="6"/><rect x="100" y="30" width="36" height="6"/><rect x="140" y="30" width="36" height="6"/>
    <rect x="180" y="30" width="36" height="6"/><rect x="220" y="30" width="36" height="6"/>
  </g>
  <g class="lblw" style="font-size:2.2px">
    <text x="78" y="34.2" class="mid">LOREM IPSUM</text><text x="118" y="34.2" class="mid">LOREM IPSUM</text><text x="158" y="34.2" class="mid">LOREM IPSUM</text>
    <text x="198" y="34.2" class="mid">LOREM IPSUM</text><text x="238" y="34.2" class="mid">LOREM IPSUM</text>
  </g>
  <g class="blue"><rect x="12" y="44" width="38" height="18"/><rect x="12" y="70" width="38" height="18"/><rect x="12" y="95" width="38" height="18"/><rect x="12" y="120" width="38" height="18"/></g>
  <g class="lblw" style="font-size:2.4px">
    <text x="18" y="52">LOREM</text><text x="18" y="55">IPSUM</text><text x="18" y="78">LOREM</text><text x="18" y="81">IPSUM</text>
    <text x="18" y="103">LOREM</text><text x="18" y="106">IPSUM</text><text x="18" y="128">LOREM</text><text x="18" y="131">IPSUM</text>
  </g>
  <g class="grey">
    <rect x="60" y="44" width="36" height="18"/><rect x="100" y="44" width="36" height="18"/><rect x="140" y="44" width="36" height="18"/><rect x="180" y="44" width="36" height="18"/><rect x="220" y="44" width="36" height="18"/>
    <rect x="60" y="70" width="36" height="18"/><rect x="100" y="70" width="36" height="18"/><rect x="140" y="70" width="36" height="18"/><rect x="180" y="70" width="36" height="18"/><rect x="220" y="70" width="36" height="18"/>
    <rect x="60" y="95" width="36" height="18"/><rect x="100" y="95" width="36" height="18"/><rect x="140" y="95" width="36" height="18"/><rect x="180" y="95" width="36" height="18"/><rect x="220" y="95" width="36" height="18"/>
    <rect x="60" y="120" width="36" height="18"/><rect x="100" y="120" width="36" height="18"/><rect x="140" y="120" width="36" height="18"/><rect x="180" y="120" width="36" height="18"/><rect x="220" y="120" width="36" height="18"/>
  </g>
  <g class="lblw" style="font-size:2.2px">
    <text x="66" y="52">LOREM</text><text x="106" y="52">LOREM</text><text x="146" y="52">LOREM</text><text x="186" y="52">LOREM</text><text x="226" y="52">LOREM</text>
    <text x="66" y="78">LOREM</text><text x="106" y="78">LOREM</text><text x="146" y="78">LOREM</text><text x="186" y="78">LOREM</text><text x="226" y="78">LOREM</text>
    <text x="66" y="103">LOREM</text><text x="106" y="103">LOREM</text><text x="146" y="103">LOREM</text><text x="186" y="103">LOREM</text><text x="226" y="103">LOREM</text>
    <text x="66" y="128">LOREM</text><text x="106" y="128">LOREM</text><text x="146" y="128">LOREM</text><text x="186" y="128">LOREM</text><text x="226" y="128">LOREM</text>
  </g>
</svg>
</section>

<!-- 4. Blue panel + photo -->
<section class="slide c4 r1" aria-label="Panel and photo slide">
<svg viewBox="0 0 276 156">
  <text x="10" y="13" class="title">EDIT TITLE HERE</text><line x1="10" y1="16" x2="22" y2="16" class="rule"/>
  <rect x="0" y="34" width="110" height="102" class="blue"/>
  <g class="pw">
    <text x="10" y="48">Somos una empresa de capital</text><text x="10" y="52">privado dedicada a la construcción de</text>
    <text x="10" y="56">proyectos tecnológicos con diseño</text><text x="10" y="60">innovador, moderno y funcional.</text>
    <text x="10" y="64">Nuestra filosofía nos ha llevado a</text><text x="10" y="68">construir proyectos únicos, pensados</text>
    <text x="10" y="72">en el bienestar integral de las</text><text x="10" y="76">familias, perdurables en el tiempo.</text>
    <text x="10" y="86">En nuestro grupo buscamos desarrollar</text><text x="10" y="90">proyectos trascendentes, buscando</text>
    <text x="10" y="94">nuevos espacios de innovación y</text><text x="10" y="98">crecimiento, con la misión de</text>
    <text x="10" y="102">transformar nuestro entorno en</text><text x="10" y="106">propuestas únicas para clientes.</text>
  </g>
  <rect x="110" y="34" width="156" height="102" fill="#8e9fb8" role="img" aria-label="Photo of an automated production line with robotic cells"/>
</svg>
</section>

<!-- 5. Team -->
<section class="slide c1 r2" aria-label="Team slide">
<svg viewBox="0 0 276 156">
  <text x="10" y="13" class="title">EDIT TITLE HERE</text><line x1="10" y1="16" x2="22" y2="16" class="rule"/>
  <rect x="0" y="66" width="276" height="40" class="blue"/>
  <g stroke="#fff" stroke-width="1.2">
    <circle cx="80" cy="62" r="21" fill="#b9c3d3" role="img" aria-label="Team member portrait"/>
    <circle cx="135" cy="62" r="21" fill="#c7ccd4" role="img" aria-label="Team member portrait"/>
    <circle cx="190" cy="62" r="21" fill="#8d96a3" role="img" aria-label="Team member portrait"/>
  </g>
  <g class="hw" style="font-size:5px;font-weight:600"><text x="80" y="95" class="mid">LOREM IPSUM</text><text x="135" y="95" class="mid">LOREM IPSUM</text><text x="190" y="95" class="mid">LOREM IPSUM</text></g>
  <g class="pw"><text x="80" y="100" class="mid">LOREM IPSUM</text><text x="135" y="100" class="mid">LOREM IPSUM</text><text x="190" y="100" class="mid">LOREM IPSUM</text></g>
</svg>
</section>

<!-- 6. Three photos -->
<section class="slide c2 r2" aria-label="Three photo slide">
<svg viewBox="0 0 276 156">
  <text x="10" y="13" class="title">EDIT TITLE HERE</text><line x1="10" y1="16" x2="22" y2="16" class="rule"/>
  <rect x="12" y="28" width="82" height="64" fill="#2f4f86" role="img" aria-label="Photo of an industrial plant at dusk"/>
  <rect x="98" y="28" width="82" height="64" fill="#5d6c86" role="img" aria-label="Photo of a heavy mining dump truck"/>
  <rect x="184" y="28" width="80" height="64" fill="#6f8aa8" role="img" aria-label="Photo of a heavy duty truck hauling a load"/>
  <rect x="12" y="90" width="252" height="2" class="blue"/>
  <g class="h"><text x="53" y="110" class="mid">LOREM IPSUM</text><text x="139" y="110" class="mid">LOREM IPSUM</text><text x="224" y="110" class="mid">LOREM IPSUM</text></g>
  <g class="p">
    <text x="53" y="116" class="mid">Lorem ipsum dolor sit amet,</text><text x="53" y="120" class="mid">consectetur adipiscing elit. Curabitur</text><text x="53" y="124" class="mid">odio ligula, ultrices eu convallis et,</text><text x="53" y="128" class="mid">condimentum at magna. Sed finibus,</text><text x="53" y="132" class="mid">felis ullamcorper interdum</text><text x="53" y="136" class="mid">ullamcorper, libero ex</text>
    <text x="139" y="116" class="mid">Lorem ipsum dolor sit amet,</text><text x="139" y="120" class="mid">consectetur adipiscing elit. Curabitur</text><text x="139" y="124" class="mid">odio ligula, ultrices eu convallis et,</text><text x="139" y="128" class="mid">condimentum at magna. Sed finibus,</text><text x="139" y="132" class="mid">felis ullamcorper interdum</text><text x="139" y="136" class="mid">ullamcorper, libero ex</text>
    <text x="224" y="116" class="mid">Lorem ipsum dolor sit amet,</text><text x="224" y="120" class="mid">consectetur adipiscing elit. Curabitur</text><text x="224" y="124" class="mid">odio ligula, ultrices eu convallis et,</text><text x="224" y="128" class="mid">condimentum at magna. Sed finibus,</text><text x="224" y="132" class="mid">felis ullamcorper interdum</text>
  </g>
</svg>
</section>

<!-- 7. Icon grid -->
<section class="slide c3 r2" aria-label="Icon grid slide">
<svg viewBox="0 0 276 156">
  <text x="10" y="13" class="title">EDIT TITLE HERE</text><line x1="10" y1="16" x2="22" y2="16" class="rule"/>
  <g class="icob">
    <path d="M42 42a4 4 0 0 1 8 0 3 3 0 0 1 0 6h-9a3 3 0 0 1 1-6z"/>
    <circle cx="91" cy="44" r="4.5"/><rect x="131" y="40" width="10" height="1.6"/><rect x="132" y="42" width="1.4" height="5"/><rect x="135.3" y="42" width="1.4" height="5"/><rect x="138.6" y="42" width="1.4" height="5"/><rect x="131" y="47" width="10" height="1.4"/>
    <circle cx="180" cy="43" r="3.2"/><circle cx="184" cy="45" r="3"/><rect x="224" y="40" width="10" height="7"/>
    <circle cx="46" cy="94" r="4.5" fill="none" stroke="var(--blue)" stroke-width="1.2"/><circle cx="91" cy="92" r="2.4"/><circle cx="94" cy="96" r="2.2"/><circle cx="88" cy="97" r="1.6"/>
    <rect x="131" y="91" width="10" height="7" rx="1"/><rect x="177" y="90" width="9" height="8" fill="none" stroke="var(--blue)" stroke-width="1.1"/><path d="M226 89h4v4h3l-5 5-5-5h3z"/>
  </g>
  <g class="h" style="font-size:2.8px">
    <text x="46" y="56" class="mid">LOREM IPSUM</text><text x="91" y="56" class="mid">LOREM IPSUM</text><text x="136" y="56" class="mid">LOREM IPSUM</text><text x="181" y="56" class="mid">LOREM IPSUM</text><text x="228" y="56" class="mid">LOREM IPSUM</text>
    <text x="46" y="106" class="mid">LOREM IPSUM</text><text x="91" y="106" class="mid">LOREM IPSUM</text><text x="136" y="106" class="mid">LOREM IPSUM</text><text x="181" y="106" class="mid">LOREM IPSUM</text><text x="228" y="106" class="mid">LOREM IPSUM</text>
  </g>
  <g class="p" style="font-size:2.2px">
    <text x="46" y="61" class="mid">Lorem ipsum dolor sit amet,</text><text x="46" y="64" class="mid">consectetur adipiscing elit.</text><text x="46" y="67" class="mid">Sed do eiusmod tempor</text>
    <text x="91" y="61" class="mid">Lorem ipsum dolor sit amet,</text><text x="91" y="64" class="mid">consectetur adipiscing elit.</text><text x="91" y="67" class="mid">Sed do eiusmod tempor</text>
    <text x="136" y="61" class="mid">Lorem ipsum dolor sit amet,</text><text x="136" y="64" class="mid">consectetur adipiscing elit.</text><text x="136" y="67" class="mid">Sed do eiusmod tempor</text>
    <text x="181" y="61" class="mid">Lorem ipsum dolor sit amet,</text><text x="181" y="64" class="mid">consectetur adipiscing elit.</text><text x="181" y="67" class="mid">Sed do eiusmod tempor</text>
    <text x="228" y="61" class="mid">Lorem ipsum dolor sit amet,</text><text x="228" y="64" class="mid">consectetur adipiscing elit.</text><text x="228" y="67" class="mid">Sed do eiusmod tempor</text>
    <text x="46" y="111" class="mid">Lorem ipsum dolor sit amet,</text><text x="46" y="114" class="mid">consectetur adipiscing elit.</text><text x="46" y="117" class="mid">Sed do eiusmod tempor</text>
    <text x="91" y="111" class="mid">Lorem ipsum dolor sit amet,</text><text x="91" y="114" class="mid">consectetur adipiscing elit.</text><text x="91" y="117" class="mid">Sed do eiusmod tempor</text>
    <text x="136" y="111" class="mid">Lorem ipsum dolor sit amet,</text><text x="136" y="114" class="mid">consectetur adipiscing elit.</text><text x="136" y="117" class="mid">Sed do eiusmod tempor</text>
    <text x="181" y="111" class="mid">Lorem ipsum dolor sit amet,</text><text x="181" y="114" class="mid">consectetur adipiscing elit.</text><text x="181" y="117" class="mid">Sed do eiusmod tempor</text>
    <text x="228" y="111" class="mid">Lorem ipsum dolor sit amet,</text><text x="228" y="114" class="mid">consectetur adipiscing elit.</text><text x="228" y="117" class="mid">Sed do eiusmod tempor</text>
  </g>
</svg>
</section>

<!-- 8. Band with icon card -->
<section class="slide c4 r2" aria-label="Icon card on band slide">
<svg viewBox="0 0 276 156">
  <text x="10" y="13" class="title">EDIT TITLE HERE</text><line x1="10" y1="16" x2="22" y2="16" class="rule"/>
  <rect x="0" y="33" width="276" height="105" fill="#2a5aa8" role="img" aria-label="Blue-toned photo of a factory floor"/>
  <rect x="95" y="50" width="181" height="66" class="white"/>
  <g class="icob">
    <path d="M122 78h12v-7l-3 2v-2l-3 2v-5h-2v5h-4z"/>
    <rect x="176" y="70" width="12" height="9" rx="1"/><rect x="179" y="68" width="6" height="3" fill="none" stroke="var(--blue)" stroke-width="1"/>
    <path d="M227 77v-4l2-4h10l2 4v4h-1v2h-2v-2h-8v2h-2v-2z"/>
  </g>
  <rect x="181" y="72" width="2" height="5" class="white"/><rect x="179.5" y="73.5" width="5" height="2" class="white"/>
  <g class="lbl" style="font-size:3.6px"><text x="128" y="90" class="mid">LOREM</text><text x="182" y="90" class="mid">LOREM</text><text x="234" y="90" class="mid">LOREM</text></g>
</svg>
</section>

<!-- 9. Numbered list + photo -->
<section class="slide c1 r3" aria-label="Numbered list slide">
<svg viewBox="0 0 276 156">
  <text x="10" y="13" class="title">EDIT TITLE HERE</text><line x1="10" y1="16" x2="22" y2="16" class="rule"/>
  <rect x="110" y="0" width="166" height="156" fill="#506c93" role="img" aria-label="Photo of a robotic welding cell with sparks"/>
  <g class="blue"><rect x="14" y="42" width="6" height="6"/><rect x="14" y="62" width="6" height="6"/><rect x="14" y="82" width="6" height="6"/><rect x="14" y="102" width="6" height="6"/><rect x="14" y="122" width="6" height="6"/></g>
  <g class="lblw" style="font-size:3.6px"><text x="17" y="46.3" class="mid">1</text><text x="17" y="66.3" class="mid">2</text><text x="17" y="86.3" class="mid">3</text><text x="17" y="106.3" class="mid">4</text><text x="17" y="126.3" class="mid">5</text></g>
  <g class="p" style="font-size:3px"><text x="27" y="46">Lorem ipsum dolor sit amet, ur</text><text x="27" y="66">Lorem ipsum dolor sit amet, ur</text><text x="27" y="86">Lorem ipsum dolor sit amet, ur</text><text x="27" y="106">Lorem ipsum dolor sit amet, ur</text><text x="27" y="126">Lorem ipsum dolor sit amet, ur</text></g>
</svg>
</section>

<!-- 10. Photo + text + icons -->
<section class="slide c2 r3" aria-label="Photo and text slide">
<svg viewBox="0 0 276 156">
  <text x="10" y="13" class="title">EDIT TITLE HERE</text><line x1="10" y1="16" x2="22" y2="16" class="rule"/>
  <rect x="14" y="28" width="101" height="106" fill="#7b8a8c" role="img" aria-label="Photo of a worker welding steel"/>
  <g class="p">
    <text x="128" y="38">Lorem ipsum dolor sit amet, consectetur adipiscing elit, sed do eiusmod</text>
    <text x="128" y="42">tincidunt ut labore et dolore magna aliqua. Ut enim ad minim veniam,</text>
    <text x="128" y="46">quis nostrud exercitation ullamco laboris nisi ut aliquip ex ea commodo</text>
    <text x="128" y="50">consequat. Duis aute irure dolor in reprehenderit in voluptate velit esse</text>
    <text x="128" y="54">cillum dolore eu fugiat nulla pariatur. Excepteur sint occaecat cupidatat</text>
    <text x="128" y="58">non proident, sunt in culpa qui officia deserunt mollit anim id est.</text>
    <text x="128" y="62">Lorem ipsum dolor sit amet, consectetur adipiscing elit, sed do eiusmod</text>
    <text x="128" y="66">tincidunt ut labore et dolore magna aliqua. Ut enim ad minim veniam,</text>
    <text x="128" y="70">quis nostrud exercitation ullamco laboris nisi ut aliquip ex ea commodo.</text>
  </g>
  <g class="icob">
    <rect x="142" y="90" width="12" height="10"/><rect x="190" y="94" width="2" height="6"/><rect x="193" y="91" width="2" height="9"/><rect x="196" y="88" width="2" height="12"/><rect x="199" y="92" width="2" height="8"/>
    <rect x="237" y="86" width="8" height="14"/><rect x="245" y="92" width="5" height="8"/>
  </g>
  <path d="M145 97l3-4 3 4z" class="white"/>
  <g class="p" style="font-size:2.2px">
    <text x="148" y="108" class="mid">Lorem ipsum dolor sit amet,</text><text x="148" y="111" class="mid">consectetur adipiscing elit.</text><text x="148" y="114" class="mid">Sed do eiusmod tempor</text>
    <text x="196" y="108" class="mid">Lorem ipsum dolor sit amet,</text><text x="196" y="111" class="mid">consectetur adipiscing elit.</text><text x="196" y="114" class="mid">Sed do eiusmod tempor</text>
    <text x="243" y="108" class="mid">Lorem ipsum dolor sit amet,</text><text x="243" y="111" class="mid">consectetur adipiscing elit.</text><text x="243" y="114" class="mid">Sed do eiusmod tempor</text>
  </g>
</svg>
</section>

<!-- 11. Split panel with icons -->
<section class="slide c3 r3" aria-label="Split panel slide">
<svg viewBox="0 0 276 156">
  <text x="10" y="13" class="title">EDIT TITLE HERE</text><line x1="10" y1="16" x2="22" y2="16" class="rule"/>
  <rect x="0" y="24" width="156" height="114" class="blue"/>
  <rect x="156" y="0" width="120" height="138" fill="#cfdde8" role="img" aria-label="Photo of a modern office interior"/>
  <g class="pw" style="font-size:3.2px;font-weight:600">
    <text x="22" y="50">Lorem ipsum dolor</text><text x="22" y="55">sit amet consectetur</text><text x="22" y="60">adipiscing elit. Cras</text>
    <text x="22" y="65">bibendum mattis leo,</text><text x="22" y="70">ac efficitur ipsum</text><text x="22" y="75">lobortis non.</text>
    <text x="22" y="80">Praesent vitae</text><text x="22" y="85">pulvinar. Lorem</text><text x="22" y="90">ipsum dolor sit amet</text>
    <text x="22" y="95">consectetur</text><text x="22" y="100">adipiscing elit. Cras</text><text x="22" y="105">bibendum mattis leo.</text>
  </g>
  <rect x="78" y="62" width="162" height="50" class="white"/>
  <g class="icob">
    <rect x="108" y="70" width="8" height="12"/><rect x="116" y="75" width="5" height="7"/>
    <rect x="158" y="72" width="12" height="9" rx="1"/>
    <path d="M213 80v-4l2-4h10l2 4v4h-1v2h-2v-2h-8v2h-2v-2z"/>
  </g>
  <rect x="163" y="74" width="2" height="5" class="white"/><rect x="161.5" y="75.5" width="5" height="2" class="white"/>
  <g class="lbl"><text x="115" y="94" class="mid">LOREM</text><text x="164" y="94" class="mid">LOREM</text><text x="220" y="94" class="mid">LOREM</text></g>
</svg>
</section>

<!-- 12. Overlay photo -->
<section class="slide c4 r3" aria-label="Overlay photo slide">
<svg viewBox="0 0 276 156">
  <text x="10" y="13" class="title">EDIT TITLE HERE</text><line x1="10" y1="16" x2="22" y2="16" class="rule"/>
  <rect x="0" y="30" width="276" height="108" fill="#6f8db3" role="img" aria-label="Photo of a large bright manufacturing hall"/>
  <rect x="0" y="30" width="125" height="108" class="blue" opacity=".92"/>
  <text x="33" y="50" class="hw" style="font-size:6px">LOREM IPSUM</text>
  <g class="pw">
    <text x="33" y="58">Lorem ipsum dolor sit amet, consectetur</text><text x="33" y="62">adipiscing elit, sed do eiusmod tempor</text>
    <text x="33" y="66">magna aliqua. Ut enim ad minim veniam,</text><text x="33" y="70">quis nostrud exercitation ullamco laboris</text>
    <text x="33" y="74">nisi ut aliquip ex ea commodo consequat.</text><text x="33" y="78">Duis aute irure dolor in reprehenderit</text>
    <text x="33" y="82">in voluptate velit esse cillum dolore</text><text x="33" y="86">eu fugiat nulla pariatur. Excepteur sint</text>
    <text x="33" y="90">occaecat cupidatat non proident, sunt</text><text x="33" y="94">in culpa qui officia deserunt mollit anim.</text>
    <text x="33" y="98">Lorem ipsum dolor sit amet, consectetur</text><text x="33" y="102">adipiscing elit, sed do eiusmod tempor</text>
    <text x="33" y="106">magna aliqua. Ut enim ad minim veniam,</text><text x="33" y="110">quis nostrud exercitation ullamco.</text>
  </g>
</svg>
</section>

<!-- 13. Two column flow -->
<section class="slide c1 r4" aria-label="Two column comparison slide">
<svg viewBox="0 0 276 156">
  <text x="10" y="13" class="title">EDIT TITLE HERE</text><line x1="10" y1="16" x2="22" y2="16" class="rule"/>
  <rect x="35" y="32" width="93" height="8" class="blue"/><rect x="148" y="32" width="94" height="8" class="grey"/>
  <text x="81" y="37.5" class="lblw mid" style="font-size:2.6px">LOREM IPSUM</text><text x="195" y="37.5" class="lblw mid" style="font-size:2.6px">LOREM IPSUM</text>
  <line x1="38" y1="40" x2="38" y2="126" stroke="var(--blue)" stroke-width="1"/>
  <line x1="152" y1="40" x2="152" y2="126" stroke="var(--grey)" stroke-width="1"/>
  <g class="blue"><circle cx="38" cy="62" r="3.5"/><circle cx="38" cy="94" r="3.5"/><circle cx="38" cy="126" r="3.5"/>
    <rect x="56" y="52" width="72" height="20" rx="3"/><rect x="56" y="84" width="72" height="20" rx="3"/><rect x="56" y="116" width="72" height="20" rx="3"/></g>
  <g class="grey"><circle cx="152" cy="62" r="3.5"/><circle cx="152" cy="94" r="3.5"/><circle cx="152" cy="126" r="3.5"/>
    <rect x="170" y="52" width="72" height="20" rx="3"/><rect x="170" y="84" width="72" height="20" rx="3"/><rect x="170" y="116" width="72" height="20" rx="3"/></g>
  <g stroke-width=".8"><line x1="41" y1="62" x2="56" y2="62" stroke="var(--blue)"/><line x1="41" y1="94" x2="56" y2="94" stroke="var(--blue)"/><line x1="41" y1="126" x2="56" y2="126" stroke="var(--blue)"/>
    <line x1="155" y1="62" x2="170" y2="62" stroke="var(--grey)"/><line x1="155" y1="94" x2="170" y2="94" stroke="var(--grey)"/><line x1="155" y1="126" x2="170" y2="126" stroke="var(--grey)"/></g>
  <g class="pw" style="font-size:3px">
    <text x="92" y="60" class="mid">Lorem ipsum dolor sit amet,</text><text x="92" y="64" class="mid">consectetur adipiscing elit, sed do</text><text x="92" y="68" class="mid">dolore magna aliqua.</text>
    <text x="92" y="92" class="mid">Lorem ipsum dolor sit amet,</text><text x="92" y="96" class="mid">consectetur adipiscing elit, sed do</text><text x="92" y="100" class="mid">dolore magna aliqua.</text>
    <text x="92" y="124" class="mid">Lorem ipsum dolor sit amet,</text><text x="92" y="128" class="mid">consectetur adipiscing elit, sed do</text><text x="92" y="132" class="mid">dolore magna aliqua.</text>
    <text x="206" y="60" class="mid">Lorem ipsum dolor sit amet,</text><text x="206" y="64" class="mid">consectetur adipiscing elit, sed do</text><text x="206" y="68" class="mid">dolore magna aliqua.</text>
    <text x="206" y="92" class="mid">Lorem ipsum dolor sit amet,</text><text x="206" y="96" class="mid">consectetur adipiscing elit, sed do</text><text x="206" y="100" class="mid">dolore magna aliqua.</text>
    <text x="206" y="124" class="mid">Lorem ipsum dolor sit amet,</text><text x="206" y="128" class="mid">consectetur adipiscing elit, sed do</text><text x="206" y="132" class="mid">dolore magna aliqua.</text>
  </g>
</svg>
</section>

<!-- 14. Devices on band -->
<section class="slide c2 r4" aria-label="Digital channels slide">
<svg viewBox="0 0 276 156">
  <text x="10" y="13" class="title">EDIT TITLE HERE</text><line x1="10" y1="16" x2="22" y2="16" class="rule"/>
  <rect x="0" y="42" width="276" height="80" class="blue"/>
  <g fill="#fff" stroke="var(--grey)" stroke-width="1.2">
    <rect x="76" y="40" width="34" height="26"/><rect x="106" y="32" width="46" height="34"/><rect x="166" y="40" width="34" height="26"/>
  </g>
  <g fill="none" stroke="var(--grey)" stroke-width=".8"><rect x="88" y="47" width="10" height="10"/><rect x="122" y="41" width="14" height="14"/><line x1="125" y1="46" x2="133" y2="46"/><line x1="125" y1="49" x2="133" y2="49"/><line x1="125" y1="52" x2="133" y2="52"/></g>
  <circle cx="183" cy="50" r="2.5" class="grey"/><path d="M178 58a5 4 0 0 1 10 0z" class="grey"/>
  <g fill="#fff"><circle cx="80" cy="99" r="6"/><circle cx="116" cy="99" r="6"/><circle cx="152" cy="99" r="6"/><circle cx="188" cy="99" r="6"/></g>
  <g class="icob"><rect x="77" y="96" width="6" height="4"/><rect x="114.5" y="95.5" width="3" height="7"/><path d="M149 101a3 3 0 0 1 6 0z"/><rect x="185" y="96" width="6" height="6"/></g>
  <g class="lblw" style="font-size:2.4px"><text x="80" y="112" class="mid">Lorem ipsum</text><text x="116" y="112" class="mid">Lorem ipsum</text><text x="152" y="112" class="mid">Lorem ipsum</text><text x="188" y="112" class="mid">Lorem ipsum</text></g>
</svg>
</section>

<!-- 15. Timeline -->
<section class="slide c3 r4" aria-label="Timeline slide">
<svg viewBox="0 0 276 156">
  <text x="10" y="13" class="title">EDIT TITLE HERE</text><line x1="10" y1="16" x2="22" y2="16" class="rule"/>
  <g stroke="var(--blue)" stroke-width=".7">
    <line x1="38" y1="140" x2="38" y2="106"/><line x1="70" y1="140" x2="70" y2="90"/><line x1="104" y1="140" x2="104" y2="104"/><line x1="138" y1="140" x2="138" y2="90"/><line x1="172" y1="140" x2="172" y2="104"/><line x1="206" y1="140" x2="206" y2="90"/><line x1="240" y1="140" x2="240" y2="104"/>
  </g>
  <g fill="#fff" stroke="var(--blue)" stroke-width=".7">
    <circle cx="38" cy="90" r="13"/><circle cx="70" cy="69" r="13"/><circle cx="104" cy="87" r="13"/><circle cx="138" cy="69" r="13"/><circle cx="172" cy="87" r="13"/><circle cx="206" cy="69" r="13"/><circle cx="240" cy="87" r="13"/>
  </g>
  <g class="blue">
    <circle cx="38" cy="109" r="5"/><circle cx="70" cy="93" r="5"/><circle cx="104" cy="107" r="5"/><circle cx="138" cy="93" r="5"/><circle cx="172" cy="107" r="5"/><circle cx="206" cy="93" r="5"/><circle cx="240" cy="107" r="5"/>
    <circle cx="38" cy="140" r="1.5"/><circle cx="70" cy="140" r="1.5"/><circle cx="104" cy="140" r="1.5"/><circle cx="138" cy="140" r="1.5"/><circle cx="172" cy="140" r="1.5"/><circle cx="206" cy="140" r="1.5"/><circle cx="240" cy="140" r="1.5"/>
  </g>
  <g class="lblw" style="font-size:2.6px"><text x="38" y="110" class="mid">2011</text><text x="70" y="94" class="mid">2012</text><text x="104" y="108" class="mid">2013</text><text x="138" y="94" class="mid">2014</text><text x="172" y="108" class="mid">2015</text><text x="206" y="94" class="mid">2016</text><text x="240" y="108" class="mid">2017</text></g>
  <g class="lbl" style="font-size:2.6px"><text x="38" y="86" class="mid">Edit Title</text><text x="70" y="65" class="mid">Edit Title</text><text x="104" y="83" class="mid">Edit Title</text><text x="138" y="65" class="mid">Edit Title</text><text x="172" y="83" class="mid">Edit Title</text><text x="206" y="65" class="mid">Edit Title</text><text x="240" y="83" class="mid">Edit Title</text></g>
  <g class="p" style="font-size:1.9px"><text x="38" y="90" class="mid">Lorem ipsum dolor</text><text x="38" y="93" class="mid">sit amet elit</text><text x="70" y="69" class="mid">Lorem ipsum dolor</text><text x="70" y="72" class="mid">sit amet elit</text><text x="104" y="87" class="mid">Lorem ipsum dolor</text><text x="104" y="90" class="mid">sit amet elit</text><text x="138" y="69" class="mid">Lorem ipsum dolor</text><text x="138" y="72" class="mid">sit amet elit</text><text x="172" y="87" class="mid">Lorem ipsum dolor</text><text x="172" y="90" class="mid">sit amet elit</text><text x="206" y="69" class="mid">Lorem ipsum dolor</text><text x="206" y="72" class="mid">sit amet elit</text><text x="240" y="87" class="mid">Lorem ipsum dolor</text><text x="240" y="90" class="mid">sit amet elit</text></g>
</svg>
</section>

<!-- 16. Photo with caption box -->
<section class="slide c4 r4" aria-label="Photo with caption slide">
<svg viewBox="0 0 276 156">
  <text x="10" y="13" class="title">EDIT TITLE HERE</text><line x1="10" y1="16" x2="22" y2="16" class="rule"/>
  <text x="16" y="28" class="lbl" style="font-size:3px">Lorem ipsum dolor sit amet, consectetur adipiscing elit. Aenean at tempor lorem. Suspendisse</text>
  <rect x="18" y="36" width="137" height="64" fill="#8b9db5" role="img" aria-label="Photo of a machining workshop with orange machinery"/>
  <rect x="155" y="36" width="107" height="64" class="blue"/>
  <text x="168" y="49" class="hw" style="font-size:3px">LOREM IPSUM</text>
  <g class="pw" style="font-size:2.2px"><text x="168" y="55">Lorem ipsum dolor sit amet, consectetur adipiscing</text><text x="168" y="58">elit. Aenean at tempor lorem. Suspendisse</text><text x="168" y="61">tellus et dolor euismod, non condimentum</text><text x="168" y="64">lectus. Sed imperdiet enim vel, et pulvinar</text><text x="168" y="67">placerat id.</text></g>
  <g class="p" style="font-size:2.4px">
    <text x="16" y="108">Nunc consequat, massa vitae dignissim elementum, nisi magna tempor sapien, efficitur luctus metus dolor in enim. Ut placerat at</text>
    <text x="16" y="111">congue ante, vitae ullamcorper risus. Nulla quis cursus, ut commodo eros pretium. Donec elementum sollicitudin aliquet. Proin</text>
    <text x="16" y="114">varius consequat lorem ipsum, ac dapibus leo porttitor eu. Pellentesque habitant morbi tristique senectus et netus.</text>
    <text x="16" y="122">Donec interdum nunc ac lacinia viverra. Praesent dapibus erat at elit eleifend consequat. Ut facilisis sem felis, sed tincidunt</text>
    <text x="16" y="125">vestibulum sed dolor lorem, in pretium diam euismod ipsum. Vestibulum tempor rhoncus. Sed nec lectus dolor.</text>
  </g>
</svg>
</section>

<!-- 17. Three column lists -->
<section class="slide c1 r5" aria-label="Three column list slide">
<svg viewBox="0 0 276 156">
  <text x="10" y="13" class="title">EDIT TITLE HERE</text><line x1="10" y1="16" x2="22" y2="16" class="rule"/>
  <rect x="6" y="34" width="86" height="7" class="blue"/><rect x="95" y="34" width="86" height="7" class="blue"/><rect x="184" y="34" width="86" height="7" class="blue"/>
  <rect x="6" y="41" width="86" height="88" fill="#eef1f6"/><rect x="95" y="41" width="86" height="88" fill="#eef1f6"/><rect x="184" y="41" width="86" height="88" fill="#eef1f6"/>
  <g stroke="var(--blue)" stroke-width=".7"><line x1="6" y1="129" x2="92" y2="129"/><line x1="95" y1="129" x2="181" y2="129"/><line x1="184" y1="129" x2="270" y2="129"/></g>
  <g class="hw" style="font-size:3px"><text x="49" y="39" class="mid">Lorem ipsum dolor</text><text x="138" y="39" class="mid">Lorem ipsum dolor</text><text x="227" y="39" class="mid">Lorem ipsum dolor</text></g>
  <g class="p" style="font-size:2.3px">
    <text x="10" y="48">• Lorem ipsum dolor sit amet, consectetur</text><text x="10" y="54">• Lorem ipsum dolor sit amet, consectetur</text><text x="10" y="60">• Lorem ipsum dolor sit amet, consectetur</text><text x="10" y="66">• Lorem ipsum dolor sit amet, consectetur</text><text x="10" y="72">• Lorem ipsum dolor sit amet, consectetur</text><text x="10" y="78">• Lorem ipsum dolor sit amet, consectetur</text><text x="10" y="84">• Lorem ipsum dolor sit amet, consectetur</text><text x="10" y="90">• Lorem ipsum dolor sit amet, consectetur</text><text x="10" y="96">• Lorem ipsum dolor sit amet, consectetur</text><text x="10" y="102">• Lorem ipsum dolor sit amet, consectetur</text><text x="10" y="108">• Lorem ipsum dolor sit amet, consectetur</text><text x="10" y="114">• Lorem ipsum dolor sit amet, consectetur</text>
    <text x="99" y="48">• Lorem ipsum dolor sit amet, consectetur</text><text x="99" y="54">• Lorem ipsum dolor sit amet, consectetur</text><text x="99" y="60">• Lorem ipsum dolor sit amet, consectetur</text><text x="99" y="66">• Lorem ipsum dolor sit amet, consectetur</text><text x="99" y="72">• Lorem ipsum dolor sit amet, consectetur</text><text x="99" y="78">• Lorem ipsum dolor sit amet, consectetur</text><text x="99" y="84">• Lorem ipsum dolor sit amet, consectetur</text><text x="99" y="90">• Lorem ipsum dolor sit amet, consectetur</text><text x="99" y="96">• Lorem ipsum dolor sit amet, consectetur</text><text x="99" y="102">• Lorem ipsum dolor sit amet, consectetur</text><text x="99" y="108">• Lorem ipsum dolor sit amet, consectetur</text><text x="99" y="114">• Lorem ipsum dolor sit amet, consectetur</text>
    <text x="188" y="48">• Lorem ipsum dolor sit amet, consectetur</text><text x="188" y="54">• Lorem ipsum dolor sit amet, consectetur</text><text x="188" y="60">• Lorem ipsum dolor sit amet, consectetur</text><text x="188" y="66">• Lorem ipsum dolor sit amet, consectetur</text><text x="188" y="72">• Lorem ipsum dolor sit amet, consectetur</text><text x="188" y="78">• Lorem ipsum dolor sit amet, consectetur</text><text x="188" y="84">• Lorem ipsum dolor sit amet, consectetur</text><text x="188" y="90">• Lorem ipsum dolor sit amet, consectetur</text><text x="188" y="96">• Lorem ipsum dolor sit amet, consectetur</text><text x="188" y="102">• Lorem ipsum dolor sit amet, consectetur</text><text x="188" y="108">• Lorem ipsum dolor sit amet, consectetur</text><text x="188" y="114">• Lorem ipsum dolor sit amet, consectetur</text>
  </g>
</svg>
</section>

<!-- 18. Table -->
<section class="slide c2 r5" aria-label="Table slide">
<svg viewBox="0 0 276 156">
  <text x="10" y="13" class="title">EDIT TITLE HERE</text><line x1="10" y1="16" x2="22" y2="16" class="rule"/>
  <rect x="20" y="46" width="238" height="10" class="blue"/>
  <rect x="20" y="56" width="238" height="13" class="glight"/><rect x="20" y="69" width="238" height="13" fill="#fff"/>
  <rect x="20" y="82" width="238" height="13" class="glight"/><rect x="20" y="95" width="238" height="13" fill="#fff"/>
  <rect x="20" y="108" width="238" height="13" class="glight"/><rect x="20" y="121" width="238" height="4" fill="#fff"/>
  <g class="hw" style="font-size:3.2px"><text x="41" y="52.5">Lorem</text><text x="103" y="52.5">Lorem</text><text x="166" y="52.5">Lorem</text><text x="225" y="52.5">Lorem</text></g>
  <g class="lbl" style="font-size:3.2px;fill:var(--grey)">
    <text x="41" y="64">Lorem</text><text x="103" y="64">Lorem</text><text x="166" y="64">Lorem</text><text x="225" y="64">Lorem</text>
    <text x="41" y="77">Lorem</text><text x="103" y="77">Lorem</text><text x="166" y="77">Lorem</text><text x="225" y="77">Lorem</text>
    <text x="41" y="90">Lorem</text><text x="103" y="90">Lorem</text><text x="166" y="90">Lorem</text><text x="225" y="90">Lorem</text>
    <text x="41" y="103">Lorem</text><text x="103" y="103">Lorem</text><text x="166" y="103">Lorem</text><text x="225" y="103">Lorem</text>
    <text x="41" y="116">Lorem</text><text x="103" y="116">Lorem</text><text x="166" y="116">Lorem</text><text x="225" y="116">Lorem</text>
  </g>
</svg>
</section>

<!-- 19. Section divider -->
<section class="slide c3 r5" aria-label="Section divider slide">
<svg viewBox="0 0 276 156">
  <defs><linearGradient id="robotPhoto" x1="0" y1="0" x2="1" y2="0"><stop offset="0" stop-color="#6e5346"/><stop offset=".5" stop-color="#c8692c"/><stop offset="1" stop-color="#7a6a60"/></linearGradient></defs>
  <rect width="276" height="156" fill="url(#robotPhoto)" role="img" aria-label="Photo of orange industrial robot arms on an assembly line"/>
  <rect x="48" y="0" width="74" height="156" class="blue" opacity=".93"/>
  <text x="85" y="54" class="hw mid" style="font-size:8px;font-weight:600">Section Title</text>
  <g class="pw" style="font-size:3.4px">
    <text x="85" y="68" class="mid">Lorem ipsum dolor sit</text><text x="85" y="73" class="mid">amet, consectetur</text><text x="85" y="78" class="mid">adipiscing elit. Curabitur</text>
    <text x="85" y="83" class="mid">odio ligula, ultrices eu</text><text x="85" y="88" class="mid">convallis et, condimentum</text><text x="85" y="93" class="mid">at magna. Sed finibus, felis</text>
    <text x="85" y="98" class="mid">ullamcorper interdum</text><text x="85" y="103" class="mid">ullamcorper, libero ex</text>
  </g>
</svg>
</section>

<!-- 20. Area chart -->
<section class="slide c4 r5" aria-label="Area chart slide">
<svg viewBox="0 0 276 156">
  <text x="10" y="13" class="title">EDIT TITLE HERE</text><line x1="10" y1="16" x2="22" y2="16" class="rule"/>
  <g stroke="#e2e3e5" stroke-width=".4"><line x1="18" y1="45" x2="196" y2="45"/><line x1="18" y1="57" x2="196" y2="57"/><line x1="18" y1="69" x2="196" y2="69"/><line x1="18" y1="81" x2="196" y2="81"/><line x1="18" y1="93" x2="196" y2="93"/></g>
  <path d="M18 105V86L60 72 102 82 146 60 196 70V105z" class="blue"/>
  <path d="M18 105V94L60 84 102 92 146 78 196 82V105z" fill="#c9cbcf"/>
  <path d="M18 105V98L60 95 102 99 146 92 196 94V105z" fill="#2c5eb3"/>
  <line x1="18" y1="105" x2="196" y2="105" stroke="var(--grey-mid)" stroke-width=".5"/>
  <g><rect x="52" y="46" width="16" height="5" class="blue"/><rect x="138" y="54" width="16" height="5" class="grey"/><rect x="180" y="62" width="16" height="5" class="grey"/><rect x="52" y="82" width="16" height="5" class="grey"/><rect x="94" y="79" width="16" height="5" class="grey"/></g>
  <g class="lblw" style="font-size:2px"><text x="60" y="49.5" class="mid">LOREM</text><text x="146" y="57.5" class="mid">LOREM</text><text x="188" y="65.5" class="mid">LOREM</text><text x="60" y="85.5" class="mid">LOREM</text><text x="102" y="82.5" class="mid">LOREM</text></g>
  <g class="p" style="font-size:2px"><text x="14" y="46" class="end">40</text><text x="14" y="58" class="end">30</text><text x="14" y="70" class="end">20</text><text x="14" y="82" class="end">10</text><text x="14" y="94" class="end">0</text>
    <text x="18" y="110">Item 1</text><text x="60" y="110">Item 2</text><text x="102" y="110">Item 3</text><text x="146" y="110">Item 4</text><text x="190" y="110">Item 5</text></g>
  <g class="blue"><circle cx="38" cy="122" r="1.5"/><circle cx="68" cy="122" r="1.5"/><circle cx="98" cy="122" r="1.5"/><circle cx="128" cy="122" r="1.5"/><circle cx="158" cy="122" r="1.5"/></g>
  <g class="p" style="font-size:2px"><text x="41" y="122.8">Lorem ipsum</text><text x="71" y="122.8">Lorem ipsum</text><text x="101" y="122.8">Lorem ipsum</text><text x="131" y="122.8">Lorem ipsum</text><text x="161" y="122.8">Lorem ipsum</text></g>
  <g class="p" style="font-size:2.3px">
    <text x="210" y="42">Lorem ipsum dolor sit amet,</text><text x="210" y="46">consectetur adipiscing elit.</text><text x="210" y="50">Sed do eiusmod tempor elit</text><text x="210" y="54">ut labore et dolore magna.</text>
    <text x="210" y="58">Ut enim ad minim veniam,</text><text x="210" y="62">quis nostrud exercitation</text><text x="210" y="66">ullamco laboris nisi ut</text><text x="210" y="70">aliquip ex ea commodo.</text>
    <text x="210" y="74">Duis aute irure dolor in</text><text x="210" y="78">reprehenderit in voluptate</text><text x="210" y="82">velit esse cillum dolore eu</text><text x="210" y="86">fugiat nulla pariatur.</text>
    <text x="210" y="90">Excepteur sint occaecat</text><text x="210" y="94">cupidatat non proident,</text><text x="210" y="98">sunt in culpa qui officia</text><text x="210" y="102">deserunt mollit anim id est.</text>
    <text x="210" y="106">Lorem ipsum dolor sit amet,</text><text x="210" y="110">consectetur adipiscing elit.</text><text x="210" y="114">Sed do eiusmod tempor.</text>
  </g>
</svg>
</section>

<!-- 21. Icon list two columns -->
<section class="slide c1 r6" aria-label="Icon list slide">
<svg viewBox="0 0 276 156">
  <text x="10" y="13" class="title">EDIT TITLE HERE</text><line x1="10" y1="16" x2="22" y2="16" class="rule"/>
  <line x1="138" y1="32" x2="138" y2="142" stroke="#d3d4d6" stroke-width=".5"/>
  <g class="blue"><circle cx="120" cy="44" r="7"/><circle cx="120" cy="70" r="7"/><circle cx="120" cy="96" r="7"/><circle cx="120" cy="122" r="7"/>
    <circle cx="156" cy="44" r="7"/><circle cx="156" cy="70" r="7"/><circle cx="156" cy="96" r="7"/><circle cx="156" cy="122" r="7"/></g>
  <g class="ico">
    <rect x="116.5" y="42" width="7" height="5"/><circle cx="120" cy="68" r="2"/><path d="M116 74a4 3 0 0 1 8 0z"/><path d="M116 95l4-2 4 2-4 2z"/><circle cx="120" cy="120" r="1.6"/><path d="M117 126l3-5 3 5z"/>
    <circle cx="156" cy="43" r="2.5"/><circle cx="156" cy="69" r="2.5"/><path d="M153 99v-5h5l2 2v3z"/><circle cx="156" cy="123" r="3"/>
  </g>
  <g class="lbl" style="font-size:2.6px">
    <text x="108" y="42" class="end">Lorem ipsum dolor</text><text x="108" y="68" class="end">Lorem ipsum dolor</text><text x="108" y="94" class="end">Lorem ipsum dolor</text><text x="108" y="120" class="end">Lorem ipsum dolor</text>
    <text x="168" y="42">Lorem ipsum dolor</text><text x="168" y="68">Lorem ipsum dolor</text><text x="168" y="94">Lorem ipsum dolor</text><text x="168" y="120">Lorem ipsum dolor</text>
  </g>
  <g class="p" style="font-size:2.2px">
    <text x="108" y="46" class="end">Lorem ipsum dolor sit amet, consectetur</text><text x="108" y="49" class="end">adipiscing elit, sed do eiusmod tempor</text>
    <text x="108" y="72" class="end">Lorem ipsum dolor sit amet, consectetur</text><text x="108" y="75" class="end">adipiscing elit, sed do eiusmod tempor</text>
    <text x="108" y="98" class="end">Lorem ipsum dolor sit amet, consectetur</text><text x="108" y="101" class="end">adipiscing elit, sed do eiusmod tempor</text>
    <text x="108" y="124" class="end">Lorem ipsum dolor sit amet, consectetur</text><text x="108" y="127" class="end">adipiscing elit, sed do eiusmod tempor</text>
    <text x="168" y="46">Lorem ipsum dolor sit amet, consectetur</text><text x="168" y="49">adipiscing elit, sed do eiusmod tempor</text>
    <text x="168" y="72">Lorem ipsum dolor sit amet, consectetur</text><text x="168" y="75">adipiscing elit, sed do eiusmod tempor</text>
    <text x="168" y="98">Lorem ipsum dolor sit amet, consectetur</text><text x="168" y="101">adipiscing elit, sed do eiusmod tempor</text>
    <text x="168" y="124">Lorem ipsum dolor sit amet, consectetur</text><text x="168" y="127">adipiscing elit, sed do eiusmod tempor</text>
  </g>
</svg>
</section>

<!-- 22. Icon boxes -->
<section class="slide c2 r6" aria-label="Icon box grid slide">
<svg viewBox="0 0 276 156">
  <text x="10" y="13" class="title">EDIT TITLE HERE</text><line x1="10" y1="16" x2="22" y2="16" class="rule"/>
  <g fill="none" stroke="var(--blue)" stroke-width=".7">
    <rect x="36" y="32" width="60" height="42"/><rect x="106" y="32" width="60" height="42"/><rect x="176" y="32" width="60" height="42"/>
    <rect x="36" y="86" width="60" height="42"/><rect x="106" y="86" width="60" height="42"/><rect x="176" y="86" width="60" height="42"/>
  </g>
  <g class="blue"><circle cx="66" cy="33" r="8"/><circle cx="136" cy="33" r="8"/><circle cx="206" cy="33" r="8"/><circle cx="66" cy="87" r="8"/><circle cx="136" cy="87" r="8"/><circle cx="206" cy="87" r="8"/></g>
  <g class="ico">
    <rect x="62" y="33" width="2" height="3"/><rect x="65" y="31" width="2" height="5"/><rect x="68" y="29" width="2" height="7"/>
    <rect x="132" y="29" width="8" height="8"/><rect x="203" y="29" width="6" height="8"/>
    <circle cx="65" cy="86" r="2.5"/><circle cx="136" cy="86" r="3"/><rect x="203" y="83" width="6" height="9" rx="1"/>
  </g>
  <g class="lbl" style="font-size:2.8px"><text x="66" y="50" class="mid">Lorem ipsum dolor</text><text x="136" y="50" class="mid">Lorem ipsum dolor</text><text x="206" y="50" class="mid">Lorem ipsum dolor</text><text x="66" y="104" class="mid">Lorem ipsum dolor</text><text x="136" y="104" class="mid">Lorem ipsum dolor</text><text x="206" y="104" class="mid">Lorem ipsum dolor</text></g>
  <g class="p" style="font-size:2.2px">
    <text x="66" y="56" class="mid">Lorem ipsum dolor sit amet,</text><text x="66" y="59" class="mid">consectetur adipiscing elit,</text><text x="66" y="62" class="mid">sed do eiusmod tempor</text>
    <text x="136" y="56" class="mid">Lorem ipsum dolor sit amet,</text><text x="136" y="59" class="mid">consectetur adipiscing elit,</text><text x="136" y="62" class="mid">sed do eiusmod tempor</text>
    <text x="206" y="56" class="mid">Lorem ipsum dolor sit amet,</text><text x="206" y="59" class="mid">consectetur adipiscing elit,</text><text x="206" y="62" class="mid">sed do eiusmod tempor</text>
    <text x="66" y="110" class="mid">Lorem ipsum dolor sit amet,</text><text x="66" y="113" class="mid">consectetur adipiscing elit,</text><text x="66" y="116" class="mid">sed do eiusmod tempor</text>
    <text x="136" y="110" class="mid">Lorem ipsum dolor sit amet,</text><text x="136" y="113" class="mid">consectetur adipiscing elit,</text><text x="136" y="116" class="mid">sed do eiusmod tempor</text>
    <text x="206" y="110" class="mid">Lorem ipsum dolor sit amet,</text><text x="206" y="113" class="mid">consectetur adipiscing elit,</text><text x="206" y="116" class="mid">sed do eiusmod tempor</text>
  </g>
</svg>
</section>

<!-- 23. Text + illustration -->
<section class="slide c3 r6" aria-label="Text and illustration slide">
<svg viewBox="0 0 276 156">
  <defs><linearGradient id="puzzleArt" x1="0" y1="0" x2="1" y2="1"><stop offset="0" stop-color="#2c5eb3"/><stop offset="1" stop-color="#1a4b9f"/></linearGradient></defs>
  <text x="10" y="13" class="title">EDIT TITLE HERE</text><line x1="10" y1="16" x2="22" y2="16" class="rule"/>
  <g class="p" style="font-size:2.3px">
    <text x="14" y="32">Lorem ipsum dolor sit amet, consectetur adipiscing elit, sed</text><text x="14" y="36">do eiusmod tempor incididunt ut labore et dolore magna aliqua.</text>
    <text x="14" y="40">Ut enim ad minim veniam, quis nostrud exercitation ullamco</text><text x="14" y="44">laboris nisi ut aliquip ex ea commodo consequat. Duis aute</text>
    <text x="14" y="48">irure dolor in reprehenderit in voluptate velit esse cillum</text><text x="14" y="52">dolore eu fugiat nulla pariatur. Excepteur sint occaecat</text>
    <text x="14" y="56">cupidatat non proident, sunt in culpa qui officia deserunt</text><text x="14" y="60">mollit anim id est laborum. Lorem ipsum dolor sit amet,</text>
    <text x="14" y="64">consectetur adipiscing elit, sed do eiusmod tempor incididunt</text><text x="14" y="68">ut labore et dolore magna aliqua. Ut enim ad minim veniam,</text>
    <text x="14" y="72">quis nostrud exercitation ullamco laboris nisi ut aliquip ex</text><text x="14" y="76">ea commodo consequat. Duis aute irure dolor in reprehenderit</text>
    <text x="14" y="80">in voluptate velit esse cillum dolore eu fugiat nulla pariatur.</text><text x="14" y="84">Excepteur sint occaecat cupidatat non proident, sunt in culpa</text>
    <text x="14" y="88">qui officia deserunt mollit anim id est laborum. Lorem ipsum</text><text x="14" y="92">dolor sit amet, consectetur adipiscing elit, sed do eiusmod</text>
    <text x="14" y="96">tempor incididunt ut labore et dolore magna aliqua. Ut enim</text><text x="14" y="100">ad minim veniam, quis nostrud exercitation ullamco laboris</text>
    <text x="14" y="104">nisi ut aliquip ex ea commodo consequat. Duis aute irure</text><text x="14" y="108">dolor in reprehenderit in voluptate velit esse cillum dolore.</text>
    <text x="14" y="112">Excepteur sint occaecat cupidatat non proident, sunt in culpa</text><text x="14" y="116">qui officia deserunt mollit anim id est laborum.</text>
  </g>
  <rect x="130" y="28" width="122" height="96" fill="url(#puzzleArt)" role="img" aria-label="Illustration of interlocking blue puzzle pieces with short labels"/>
</svg>
</section>

<!-- 24. Closing -->
<section class="slide c4 r6" aria-label="Closing slide">
<svg viewBox="0 0 276 156">
  <defs><linearGradient id="closePhoto" x1="0" y1="0" x2="1" y2="1"><stop offset="0" stop-color="#2e5fb2"/><stop offset=".6" stop-color="#1a4b9f"/><stop offset="1" stop-color="#143f88"/></linearGradient></defs>
  <rect width="276" height="156" fill="url(#closePhoto)" role="img" aria-label="Blue-toned photo of a precision machining workstation"/>
  <line x1="62" y1="56" x2="212" y2="56" stroke="#fff" stroke-width=".6"/>
  <line x1="62" y1="90" x2="212" y2="90" stroke="#fff" stroke-width=".6"/>
  <text x="138" y="79" class="mid" style="font-size:15px;font-weight:700;fill:#fff">THANK YOU</text>
</svg>
</section>

</body>
</html>
```